Mistvale Botanica Teas needs a website with shopping cart

We are a herbal tea business that hand blends organic tea recipes for medicinal purposes and for customer enjoyment. We require a website that represents our elegant brand and our connection to plant medicine. We will require a home page, a products page, a contact us page with form and an information page. We will need to be able to photograph our teas and upload the images to the products page along with changing pricing and shipping costs, and the ability to add/change information and images to our information page as this page will be mostly about the different herbs we will use in the teas. Our teas will be 'loose leaf' (not in tea bags) and will be sold in glass jars. At this stage we only intend to use CoinLoop as a method of payment for overseas customers and direct credit for New Zealand customers.

Target Market(s)

Tea drinkers, women, people interested in health/herbs, people looking for gifts

Industry/Entity Type

Shopping

Logo Text

Mistvale Botanica Teas

Coding

Coded - Design and coding required

Number of Pages Required

4 page

Font styles to use
Decorative

Requirements
Must have
• I am a herbalist and love plants, flowers and nature so would like the overall website and logo to represent this. I have attached the logo I had designed several years ago for myself as inspiration - the graduated greens are great and very vibrant which I like (sorry about the quality, I couldn't find the source files - NEW SOURCE FILE ADDED 23/04/15). This is an upmarket, niche product which is elegant and healthy.

```html
<!DOCTYPE html>
<html lang="en">
<head>
<meta charset="utf-8">
<title>Mistvale Botanica Teas – Contact us</title>
<link rel="stylesheet" href="https://fonts.googleapis.com/css2?family=Marcellus&display=swap">
<style>
:root{
  --canvas:#000;
  --white:#fff;
  --leaf:#8bc34a;
  --leaf-dark:#6fa52f;
  --leaf-deep:#4e8a1e;
  --lime:#b6d94a;
  --sun:#f6c030;
  --sky:#29abe2;
  --ink:#4a3b2a;
  --muted:#6b6b6b;
  --night:#333333;
  --night-2:#2a2a2a;
  --pink:#e0307a;
}
*{box-sizing:border-box;margin:0;padding:0}
html,body{width:900px;height:1200px;overflow:hidden;background:var(--canvas)}
body{position:relative;font-family:"Marcellus",serif;color:var(--ink)}
.abs{position:absolute}
.page{left:65px;top:198px;width:770px;height:804px;background:var(--white);overflow:hidden}

/* header */
.brand{left:158px;top:8px;width:110px;text-align:center}
.brand-mark{display:block;margin:0 auto 3px;width:22px;height:22px;border-radius:50%;background:var(--leaf-dark)}
.brand-name{font-size:9.5px;color:var(--leaf-deep);letter-spacing:.3px;line-height:1.1}
.brand-tag{font-size:3.6px;color:var(--leaf-deep);letter-spacing:.3px;margin-top:2px;text-transform:uppercase}
.icon-btn{width:15px;height:15px;border-radius:50%;background:var(--leaf);top:8px}
.acct-btn{top:8px;height:17px;font-size:7.5px;color:var(--white);text-align:center;line-height:17px;border-radius:2px;letter-spacing:.3px}
.login{left:508px;width:45px;background:var(--leaf)}
.signup{left:557px;width:45px;background:var(--sun)}
.nav a{position:absolute;top:34px;font-size:10.5px;color:var(--ink);text-decoration:none;white-space:nowrap}
.nav .current{color:var(--leaf-dark)}

/* band */
.title-band{left:0;top:60px;width:770px;height:38px;background:var(--leaf);border-bottom:3px solid var(--leaf-dark);color:var(--white);font-size:14px;text-align:center;line-height:36px;letter-spacing:.5px}

.photo{background:linear-gradient(135deg,#d7ee7a,#8cc63f 45%,#4f8d1f)}
.photo-soft{background:linear-gradient(160deg,#b9dc55,#7fb832 60%,#9ccd45)}
.contact-panel{left:150px;top:98px;width:470px;height:304px;background:var(--white)}
.map{left:6px;top:7px;width:458px;height:140px;background:linear-gradient(135deg,#e9e6df,#dcd8cf)}
.map-pin{left:200px;top:52px}
.map-label{left:212px;top:72px;font-size:7px;color:#9c1b1b;font-family:Arial,sans-serif;font-weight:bold}

.section-head{font-size:8.5px;color:var(--ink);letter-spacing:.3px;border-bottom:1px solid var(--leaf);padding-bottom:4px}
.field{background:var(--leaf);color:var(--white);font-size:5.8px;padding:8px 10px;border-radius:1px}
.send{left:8px;top:281px;width:88px;height:22px;background:var(--sky);color:var(--white);font-size:7.5px;text-align:center;line-height:22px;letter-spacing:.4px}
.addr{left:360px;top:178px;width:104px;font-size:6px;line-height:8.5px;color:var(--muted)}
.addr .lbl{color:var(--leaf-dark);margin-top:8px}
.addr .tel{color:var(--sky)}
.addr .free{color:var(--pink)}
.dot{display:inline-block;width:6px;height:6px;border-radius:50%;background:var(--sky);vertical-align:-1px}

.hear{left:0;top:402px;width:770px;text-align:center;color:var(--leaf-dark);font-size:12px}
.intro{left:216px;top:430px;width:352px;font-size:7.5px;line-height:8px;color:var(--ink)}
.intro p+p{margin-top:8px}
.intro .link{color:var(--leaf-dark)}

.promo-text{left:150px;top:488px;width:470px;text-align:center;color:var(--white);font-size:29px;line-height:38px}
.shop{left:347px;top:599px;width:70px;height:18px}
.shop-cart{left:0;top:0;width:18px;height:18px;background:var(--leaf)}
.shop-label{left:18px;top:0;width:52px;height:18px;background:var(--night-2);color:var(--white);font-size:7px;line-height:18px;text-align:center}

.signup-bar{left:0;top:623px;width:770px;height:40px;background:var(--night)}
.signup-text{left:168px;top:10px;color:var(--white);font-size:17px}
.subscribe{left:523px;top:9px;width:62px;height:23px;background:var(--leaf);color:var(--white);font-size:9.5px;line-height:23px;text-align:center}

.footer{left:150px;top:663px;width:470px;height:141px;background:var(--night)}
.col{top:6px;color:var(--white);font-size:8px}
.col h3{font-weight:normal;font-size:8.5px;margin-bottom:16px;letter-spacing:.3px}
.col li{list-style:none;line-height:11.5px;font-size:7.5px}
.blog-img{width:74px;height:52px;background:linear-gradient(135deg,#eee,#9aa,#556)}
.blog-text{font-size:6px;line-height:8.5px;margin-top:9px;width:92px}
.blog-text span{color:var(--leaf)}
.social{display:flex;gap:14px;margin-left:14px}
.social i{width:14px;height:16px;background:var(--leaf)}
.contact-line{font-size:6.5px;line-height:9px;display:flex;gap:8px;margin-top:5px}
.contact-line svg{flex:none}
</style>
</head>
<body>
<div class="abs page">
  <header>
    <div class="abs brand">
      <span class="brand-mark"></span>
      <div class="brand-name">MISTVALE BOTANICA TEAS</div>
      <div class="brand-tag">herbal blends for body and calm</div>
    </div>
    <div class="abs icon-btn" style="left:463px"></div>
    <div class="abs icon-btn" style="left:483px"></div>
    <div class="abs acct-btn login">LOG IN</div>
    <div class="abs acct-btn signup">SIGN UP</div>
    <nav class="nav">
      <a style="left:362px">Home</a>
      <a style="left:414px">Our products</a>
      <a style="left:486px">Information</a>
      <a class="current" style="left:557px">Contact us</a>
    </nav>
    <svg class="abs" style="left:548px;top:48px" width="32" height="12" viewBox="0 0 32 12"><path d="M2 8 Q14 -2 30 4 Q18 14 2 8Z" fill="var(--leaf)"/></svg>
  </header>

  <div class="abs title-band">CONTACT US</div>

  <div class="abs photo" role="img" aria-label="Close-up photo of fresh green tea leaves" style="left:0;top:98px;width:150px;height:304px"></div>
  <div class="abs photo-soft" role="img" aria-label="Soft-focus green tea leaf background" style="left:620px;top:98px;width:150px;height:304px"></div>

  <section class="abs contact-panel">
    <div class="abs map" role="img" aria-label="Street map showing the shop location"></div>
    <svg class="abs map-pin" width="10" height="16" viewBox="0 0 10 16"><path d="M5 16 L1 7 A4.5 4.5 0 1 1 9 7Z" fill="#d32f2f"/><circle cx="5" cy="5" r="1.6" fill="#fff"/></svg>
    <div class="abs map-label">27 Willowbank Rd</div>

    <div class="abs section-head" style="left:6px;top:155px;width:340px">CONTACT INFORMATION</div>
    <div class="abs section-head" style="left:357px;top:155px;width:107px">ADDRESS</div>

    <div class="abs field" style="left:8px;top:179px;width:104px;height:22px">Your Name *</div>
    <div class="abs field" style="left:125px;top:179px;width:104px;height:22px">Your Email *</div>
    <div class="abs field" style="left:241px;top:179px;width:104px;height:22px">Phone No. *</div>
    <div class="abs field" style="left:8px;top:212px;width:104px;height:22px">Your City *</div>
    <div class="abs field" style="left:125px;top:212px;width:220px;height:56px">Your Message *</div>
    <div class="abs field" style="left:8px;top:246px;width:104px;height:22px">Country</div>
    <div class="abs send">SEND MESSAGE</div>

    <div class="abs addr">
      <p>You may also contact us by phone at <span class="dot"></span> <span class="tel">1-800-555-0142</span> <span class="free">FREE</span> or <span class="dot"></span> <span class="tel">1-800-555-0142</span> <span class="free">FREE</span></p>
      <p class="lbl">ADDRESS 1:</p>
      <p>The Company Name Inc. 214 Fernhollow Lane, Ashby, KT 18</p>
      <p class="lbl">ADDRESS 2:</p>
      <p>The Company Name Inc. 214 Fernhollow Lane, Ashby, KT 18</p>
    </div>
  </section>

  <h2 class="abs hear" style="font-weight:normal">We want to hear from you!</h2>
  <div class="abs intro">
    <p>Please refer to our <span class="link">FAQS</span> section to see if your question has already been answered there. You can also find out about the stores near you where our products are sold by checking our <span class="link">STORE LOCATOR.</span></p>
    <p>If you have a specific question that isn't answered in the <span class="link">FAQS</span>, please fill in the fields to the right and send an e-mail to our customer service department.</p>
  </div>

  <div class="abs photo-soft" role="img" aria-label="Blurred green garden background" style="left:0;top:486px;width:770px;height:137px"></div>
  <div class="abs" role="img" aria-label="Photo of an iced green tea drink with mint leaves" style="left:150px;top:486px;width:470px;height:137px;background:linear-gradient(120deg,#a8d048,#6ea82c 50%,#b7d968)"></div>
  <div class="abs promo-text">We Offer<br>Premium Quality<br>Herbal Tea</div>
  <div class="abs shop">
    <div class="abs shop-cart">
      <svg width="18" height="18" viewBox="0 0 18 18"><path d="M4 5h2l1.5 6h6l1.2-4.5H7" fill="none" stroke="#fff" stroke-width="1.3"/><circle cx="8" cy="13.5" r="1" fill="#fff"/><circle cx="13" cy="13.5" r="1" fill="#fff"/></svg>
    </div>
    <div class="abs shop-label">SHOP NOW</div>
  </div>

  <div class="abs signup-bar">
    <div class="abs signup-text">@&nbsp; Get 15 % off teas with e-mail sign-up!</div>
    <div class="abs subscribe">SUBSCRIBE</div>
  </div>

  <div class="abs photo" role="img" aria-label="Photo of terraced tea plantation fields" style="left:0;top:663px;width:150px;height:141px"></div>
  <div class="abs photo" role="img" aria-label="Photo of terraced tea plantation rows" style="left:620px;top:663px;width:150px;height:141px"></div>

  <footer class="abs footer">
    <div class="abs col" style="left:30px">
      <h3>INFORMATION</h3>
      <ul><li>About Us</li><li>Our Products</li><li>Customer Service</li><li>Terms &amp; Conditions</li><li>Privacy Policy</li><li>Site Map</li><li>FAQ</li><li>Contact Us</li></ul>
    </div>
    <div class="abs col" style="left:148px">
      <h3>MY ACCOUNT</h3>
      <ul><li>Sign In</li><li>View Cart</li><li>My Wishlist</li><li>Track My Order</li><li>Orders &amp; Returns</li><li>Help</li></ul>
    </div>
    <div class="abs col" style="left:249px">
      <h3 style="margin-left:12px">TEA TALK BLOG</h3>
      <div class="blog-img" role="img" aria-label="Blog photo of a seedling sprouting in soil" style="margin-left:8px"></div>
      <p class="blog-text">Stay Healthy This Spring! Ayurveda is all about balance - how to... <span>Read More »</span></p>
    </div>
    <div class="abs col" style="left:356px">
      <h3 style="margin-left:30px;margin-bottom:14px">FOLLOW US</h3>
      <div class="social"><i></i><i></i><i></i></div>
      <h3 style="margin:14px 0 8px 30px">CONTACTS</h3>
      <div class="contact-line">
        <svg width="9" height="9" viewBox="0 0 10 10"><path d="M5 10 L1.5 4.5 A3.5 3.5 0 1 1 8.5 4.5Z" fill="var(--leaf)"/></svg>
        <span>My Company , 62 Linden<br>Crescent, Ashby KT4<br>2LP</span>
      </div>
      <div class="contact-line" style="margin-top:8px">
        <svg width="9" height="9" viewBox="0 0 10 10"><path d="M2 1l2 0 1 2.5-1.3 1a6 6 0 0 0 2.8 2.8l1-1.3 2.5 1v2a1 1 0 0 1-1 1A8 8 0 0 1 1 2a1 1 0 0 1 1-1z" fill="var(--leaf)"/></svg>
        <span>+ 1(800)555-0199</span>
      </div>
    </div>
  </footer>
</div>
</body>
</html>
```